Design a Mobile App for Landscape Businesses

This project is to design the first three screens for a mobile app for Landscape and Lawncare businesses. This app will serve as a directory for homeowners to locate landscape and lawn care businesses and for landscape businesses and contractors to run their business. See the attached PDF for more information and example
Here is the link to the description https://brevlinq.test/k3r92P

Target Market(s)

Landscape and lawn care business, gardeners, home owners

Industry/Entity Type

Landscape Gardening

Logo Text

Quillmoray

Colors

Designer to choose colors to be used in the design.

```html
<!DOCTYPE html>
<html lang="en">
<head>
<meta charset="UTF-8">
<title>Quillmoray – Directory</title>
<link href="https://fonts.googleapis.com/css2?family=Montserrat:wght@400;500;600&display=swap" rel="stylesheet">
<style>
:root{
  --brand-blue:#0b6fd8;
  --white:#ffffff;
  --text-dark:#555555;
  --text-title:#6f6f6f;
  --text-muted:#8a8a8a;
  --lawn-top:#2e3b2a;
  --lawn-mid:#3f7a32;
  --lawn-low:#5fa046;
}
*{box-sizing:border-box;margin:0;padding:0}
html,body{width:675px;height:1200px;overflow:hidden;background:var(--white);font-family:'Montserrat',sans-serif}
.app{position:relative;width:675px;height:1200px;overflow:hidden}
.app-header{position:absolute;left:0;top:0;width:675px;height:79px;background:var(--brand-blue);display:flex;align-items:center;justify-content:center;gap:10px}
.brand-mark{width:22px;height:22px;background:var(--white)}
.brand-name{color:var(--white);font-weight:600;font-size:22px}
.sort-bar{position:absolute;top:126px;left:0;width:675px;height:32px;font-size:19px;color:var(--text-dark)}
.sort-label{position:absolute;left:114px;top:5px}
.sort-option{position:absolute;top:5px}
.sort-option.is-active{left:206px;top:0;width:105px;height:32px;background:var(--brand-blue);color:var(--white);display:flex;align-items:center;justify-content:center;font-weight:500}
.listing{position:absolute;left:0;width:675px;height:150px}
.listing-photo{position:absolute;left:21px;top:0;width:187px;height:127px;background:linear-gradient(180deg,var(--lawn-top) 0%,var(--lawn-top) 25%,var(--lawn-mid) 45%,var(--lawn-low) 100%)}
.listing-title{position:absolute;left:229px;top:4px;font-size:29px;font-weight:500;color:var(--text-title);letter-spacing:.5px}
.listing-tagline{position:absolute;left:229px;top:38px;font-size:14.5px;line-height:17px;color:var(--text-muted);text-transform:uppercase;width:230px}
.quote-button{position:absolute;left:229px;top:84px;width:140px;height:42px;background:var(--brand-blue);color:var(--white);font-size:16px;display:flex;align-items:center;justify-content:center;box-shadow:0 3px 5px rgba(0,0,0,.25)}
.listing-info{position:absolute;left:508px;font-size:20px;color:var(--text-dark);white-space:nowrap}
.info-serving{top:10px}
.info-area{top:52px}
.info-phone{top:97px}
</style>
</head>
<body>
<div class="app">
  <header class="app-header">
    <span class="brand-mark"></span>
    <span class="brand-name">Quillmoray</span>
  </header>

  <nav class="sort-bar">
    <span class="sort-label">Sort by:</span>
    <span class="sort-option is-active">Distance</span>
    <span class="sort-option" style="left:330px">Offering A Deal</span>
    <span class="sort-option" style="left:510px">Price</span>
  </nav>

  <section class="listing" style="top:201px">
    <div class="listing-photo" role="img" aria-label="Freshly striped lawn with trees"></div>
    <h2 class="listing-title">Rin's Turf</h2>
    <p class="listing-tagline">Our level of commitment has no limit</p>
    <div class="quote-button">Quote please</div>
    <span class="listing-info info-serving">serving</span>
    <span class="listing-info info-area">Marvela,eldoraa</span>
    <span class="listing-info info-phone">+01555018274</span>
  </section>

  <section class="listing" style="top:358px">
    <div class="listing-photo" role="img" aria-label="Freshly striped lawn with trees"></div>
    <h2 class="listing-title">Rin's Turf</h2>
    <p class="listing-tagline">Our level of commitment has no limit</p>
    <div class="quote-button">Quote please</div>
    <span class="listing-info info-serving">serving</span>
    <span class="listing-info info-area">Marvela,eldoraa</span>
    <span class="listing-info info-phone">+01555018274</span>
  </section>

  <section class="listing" style="top:516px">
    <div class="listing-photo" role="img" aria-label="Freshly striped lawn with trees"></div>
    <h2 class="listing-title">Rin's Turf</h2>
    <p class="listing-tagline">Our level of commitment has no limit</p>
    <div class="quote-button">Quote please</div>
    <span class="listing-info info-serving">serving</span>
    <span class="listing-info info-area">Marvela,eldoraa</span>
    <span class="listing-info info-phone">+01555018274</span>
  </section>

  <section class="listing" style="top:673px">
    <div class="listing-photo" role="img" aria-label="Freshly striped lawn with trees"></div>
    <h2 class="listing-title">Rin's Turf</h2>
    <p class="listing-tagline">Our level of commitment has no limit</p>
    <div class="quote-button">Quote please</div>
    <span class="listing-info info-serving">serving</span>
    <span class="listing-info info-area">Marvela,eldoraa</span>
    <span class="listing-info info-phone">+01555018274</span>
  </section>

  <section class="listing" style="top:831px">
    <div class="listing-photo" role="img" aria-label="Freshly striped lawn with trees"></div>
    <p class="listing-tagline">Our level of commitment has no limit</p>
    <div class="quote-button">Quote please</div>
    <span class="listing-info info-area">Marvela,eldoraa</span>
    <span class="listing-info info-phone">+01555018274</span>
  </section>

  <section class="listing" style="top:988px">
    <div class="listing-photo" role="img" aria-label="Freshly striped lawn with trees"></div>
    <h2 class="listing-title">Rin's Turf</h2>
    <p class="listing-tagline">Our level of commitment has no limit</p>
    <div class="quote-button">Quote please</div>
    <span class="listing-info info-serving">serving</span>
    <span class="listing-info info-area">Marvela,eldoraa</span>
    <span class="listing-info info-phone">+01555018274</span>
  </section>

  <section class="listing" style="top:1146px">
    <div class="listing-photo" role="img" aria-label="Freshly striped lawn with trees"></div>
    <h2 class="listing-title">Rin's Turf</h2>
    <p class="listing-tagline">Our level of commitment has no limit</p>
    <div class="quote-button">Quote please</div>
    <span class="listing-info info-serving">serving</span>
    <span class="listing-info info-area">Marvela,eldoraa</span>
    <span class="listing-info info-phone">+01555018274</span>
  </section>
</div>
</body>
</html>
```